Bref créative
Velt Heating Ltd
business card & stationary package
Modern
Dorin Maleck, Owner
Government Certified Technician
(no address please)
Would also like a card made for:
Luc Brantley
info@veltheat.ca
www.veltheat.ca
Serving the North Shore of Vancouver since 1994
Air Conditioners
BBQs
Boilers
Firepits
Fireplaces
Furnaces
Gas Outlet Boxes
Patio Heaters
Pool Heaters
Heat Pumps
HRV Units
There is a spelling error under Dorin Maleck, Owner... there should be an 'n' in government.

```html
<!DOCTYPE html>
<html lang="en">
<head>
<meta charset="utf-8">
<title>Velt Heating Ltd – Stationery Package</title>
<link rel="stylesheet" href="https://fonts.googleapis.com/css2?family=Open+Sans:wght@400;700&display=swap">
<style>
  :root {
    --stage: #e6e7e8;
    --paper: #ffffff;
    --blue: #1f7fc3;
    --blue-deep: #0d5a97;
    --green: #7cb82f;
    --orange: #f39221;
    --ink: #4a4a4a;
    --ink-soft: #8a8a8a;
  }
  * { box-sizing: border-box; margin: 0; padding: 0; }
  html, body { width: 1200px; height: 271px; overflow: hidden; }
  body {
    position: relative;
    background: var(--stage);
    font-family: "Open Sans", Arial, sans-serif;
    color: var(--ink);
  }
  .item {
    position: absolute;
    background: var(--paper);
    box-shadow: 0 1px 3px rgba(0,0,0,.25);
    overflow: hidden;
  }
  .brand {
    display: flex; align-items: center; gap: 3px;
    font-weight: 700; color: var(--blue-deep); white-space: nowrap;
  }
  .brand .dot { border-radius: 50%; background: var(--blue); flex: none; }
  .swoosh { position: absolute; inset: 0; width: 100%; height: 100%; }
  .tiny { font-size: 3px; line-height: 1.45; }

  /* business cards */
  .card { width: 64px; height: 36px; }
  .card--front { left: 7px; top: 84px; }
  .card--back { left: 7px; top: 123px; background: var(--blue); }
  .card--second { left: 7px; top: 162px; }
  .card .brand { position: absolute; left: 5px; top: 6px; font-size: 5px; }
  .card .brand .dot { width: 5px; height: 5px; }
  .card .details { position: absolute; left: 5px; bottom: 5px; font-size: 2.6px; line-height: 1.4; }
  .card--back .details { color: #fff; left: 5px; top: 10px; font-size: 3px; }
  .note { left: 7px; top: 205px; width: 64px; height: 48px; }
  .note .brand { position: absolute; left: 5px; top: 5px; font-size: 4px; }
  .note .brand .dot { width: 4px; height: 4px; background: var(--green); }
  .note .msg { position: absolute; left: 5px; top: 18px; font-size: 4px; color: var(--green); font-weight: 700; }

  /* letterheads */
  .letterhead { top: 84px; width: 138px; height: 176px; }
  .letterhead--one { left: 163px; }
  .letterhead--two { left: 307px; }
  .letterhead .brand { position: absolute; left: 10px; top: 9px; font-size: 7px; }
  .letterhead .brand .dot { width: 7px; height: 7px; }
  .letterhead .body { position: absolute; left: 10px; top: 34px; width: 102px; }
  .letterhead .body p { margin-bottom: 3px; }
  .letterhead .sign { margin-top: 8px; }
  .letterhead .footer { position: absolute; left: 10px; bottom: 6px; font-size: 2.6px; color: var(--ink-soft); }

  /* centre card and slip */
  .card-large { left: 547px; top: 110px; width: 108px; height: 46px; }
  .card-large .brand { position: absolute; left: 8px; top: 8px; font-size: 8px; }
  .card-large .brand .dot { width: 8px; height: 8px; }
  .card-large .details { position: absolute; left: 8px; bottom: 6px; font-size: 3px; line-height: 1.4; }
  .slip { left: 555px; top: 228px; width: 100px; height: 14px; }
  .slip .tag { position: absolute; left: 6px; top: 4px; font-size: 3px; }

  /* envelopes */
  .envelope { left: 713px; width: 120px; }
  .envelope--colour { top: 100px; height: 72px; background: linear-gradient(180deg, var(--orange) 0%, #f7b04c 35%, #ffffff 48%, var(--blue) 62%, var(--blue-deep) 100%); }
  .envelope--colour .brand { position: absolute; left: 50%; top: 50%; transform: translate(-50%,-50%); font-size: 4px; color: var(--blue-deep); }
  .envelope--colour .brand .dot { width: 6px; height: 6px; background: var(--blue-deep); }
  .envelope--white { top: 187px; height: 52px; }
  .envelope--white .band { position: absolute; left: 0; right: 0; top: 14px; height: 5px; background: linear-gradient(90deg, var(--blue), var(--green) 60%, var(--orange)); }
  .envelope--white .brand { position: absolute; left: 6px; top: 3px; font-size: 4px; }
  .envelope--white .brand .dot { width: 4px; height: 4px; }

  /* presentation folder */
  .folder { top: 72px; height: 192px; }
  .folder--inside { left: 840px; width: 172px; background: linear-gradient(160deg, #3b99d6, var(--blue) 50%, var(--blue-deep)); }
  .folder--inside .pocket { position: absolute; left: 0; right: 0; bottom: 0; height: 58px; background: var(--blue-deep); opacity: .55; }
  .folder--cover { left: 1014px; width: 174px; }
  .folder--cover .brand { position: absolute; left: 34px; top: 44px; font-size: 11px; }
  .folder--cover .brand .dot { width: 12px; height: 12px; }
  .folder--cover .tagline { position: absolute; left: 34px; top: 62px; font-size: 3.4px; color: var(--green); }
  .folder--cover .slot { position: absolute; right: 18px; bottom: 12px; width: 38px; height: 16px; background: #fff; box-shadow: 0 0 2px rgba(0,0,0,.3); }
</style>
</head>
<body>

  <!-- Business cards -->
  <section class="item card card--front">
    <div class="brand"><span class="dot"></span>Velt Heating Ltd</div>
    <div class="details"><b>Dorin Maleck</b>, Owner<br>Government Certified Technician<br>info@veltheat.ca</div>
  </section>
  <section class="item card card--back">
    <div class="details"><b>Velt Heating Ltd</b><br>604-555-0148<br>www.veltheat.ca</div>
  </section>
  <section class="item card card--second">
    <div class="brand"><span class="dot"></span>Velt Heating Ltd</div>
    <div class="details"><b>Luc Brantley</b><br>info@veltheat.ca<br>www.veltheat.ca</div>
  </section>
  <section class="item note">
    <div class="brand"><span class="dot"></span>Velt Heating Ltd</div>
    <div class="msg">Thank you for your business</div>
  </section>

  <!-- Letterheads -->
  <section class="item letterhead letterhead--one">
    <svg class="swoosh" viewBox="0 0 138 176" preserveAspectRatio="none" aria-hidden="true">
      <path d="M128 0 Q116 90 138 176 L138 0Z" fill="var(--blue)"/>
      <path d="M124 0 Q112 90 132 176 L136 176 Q116 90 128 0Z" fill="var(--green)"/>
      <path d="M0 168 Q70 160 138 172 L138 176 L0 176Z" fill="var(--orange)"/>
    </svg>
    <div class="brand"><span class="dot"></span>Velt Heating Ltd</div>
    <div class="body tiny">
      <p>Dear Client,</p>
      <p>Thank you for choosing us for your home heating needs. Our certified team installs and services furnaces, boilers, fireplaces and heat pumps across the North Shore. We look forward to keeping your home warm and safe all year.</p>
      <p class="sign">Sincerely,<br><b>Dorin Maleck</b>, Owner</p>
    </div>
    <div class="footer">info@veltheat.ca · www.veltheat.ca</div>
  </section>
  <section class="item letterhead letterhead--two">
    <svg class="swoosh" viewBox="0 0 138 176" preserveAspectRatio="none" aria-hidden="true">
      <path d="M128 0 Q116 90 138 176 L138 0Z" fill="var(--blue)"/>
      <path d="M124 0 Q112 90 132 176 L136 176 Q116 90 128 0Z" fill="var(--green)"/>
      <path d="M0 168 Q70 160 138 172 L138 176 L0 176Z" fill="var(--orange)"/>
    </svg>
    <div class="brand"><span class="dot"></span>Velt Heating Ltd</div>
    <div class="body tiny">
      <p>Dear Client,</p>
      <p>Thank you for choosing us for your home heating needs. Our certified team installs and services furnaces, boilers, fireplaces and heat pumps across the North Shore. We look forward to keeping your home warm and safe all year.</p>
      <p class="sign">Sincerely,<br><b>Luc Brantley</b></p>
    </div>
    <div class="footer">info@veltheat.ca · www.veltheat.ca</div>
  </section>

  <!-- Centre card and slip -->
  <section class="item card-large">
    <div class="brand"><span class="dot"></span>Velt Heating Ltd</div>
    <div class="details"><b>Dorin Maleck</b>, Owner · Government Certified Technician<br>info@veltheat.ca · www.veltheat.ca</div>
  </section>
  <section class="item slip">
    <div class="tag">Serving the North Shore of Vancouver since 1994</div>
  </section>

  <!-- Envelopes -->
  <section class="item envelope envelope--colour">
    <div class="brand"><span class="dot"></span>Velt Heating Ltd</div>
  </section>
  <section class="item envelope envelope--white">
    <div class="brand"><span class="dot"></span>Velt Heating Ltd</div>
    <div class="band"></div>
  </section>

  <!-- Presentation folder -->
  <section class="item folder folder--inside">
    <div class="pocket"></div>
  </section>
  <section class="item folder folder--cover">
    <svg class="swoosh" viewBox="0 0 174 192" preserveAspectRatio="none" aria-hidden="true">
      <path d="M0 150 Q90 120 174 140 L174 192 L0 192Z" fill="var(--blue)"/>
      <path d="M0 146 Q90 114 174 134 L174 140 Q90 120 0 150Z" fill="var(--green)"/>
      <path d="M0 142 Q90 108 174 128 L174 134 Q90 114 0 146Z" fill="var(--orange)"/>
    </svg>
    <div class="brand"><span class="dot"></span>Velt Heating Ltd</div>
    <div class="tagline">Serving the North Shore of Vancouver since 1994</div>
    <div class="slot"></div>
  </section>

</body>
</html>
```